Zentrova - Creative Automation

We are a software house for Audio Visual Systems integration/automation and home automation. we develop innovative software to automate a variety of devices mainly related to audio visuals and we design touch panel user interfaces to control these systems.

We would like to see designs that stick to our colours and theme, which you can find on our webpage www.zentrova.com.au

The final design should communicate touch panels, innovation, software and automation.

Industry/Entity Type

Software

Requirements
Must have
• The business card must show the following information:
Name example : Derek Malloway
Qualification example: B Eng ICT(CompSys) Dip EngPrac
Title example : Control Systems Programmer
Mobile Phone, Company phone, Email address ,Company website

```html
<!DOCTYPE html>
<html lang="en">
<head>
<meta charset="UTF-8">
<title>Zentrova – Business Card</title>
<link rel="stylesheet" href="https://fonts.googleapis.com/css2?family=Baloo+2:wght@600;700&family=Ubuntu:ital,wght@0,400;0,500;1,400;1,500&display=swap">
<style>
  :root {
    --stage: #e6e8ea;
    --card: #ffffff;
    --brand-green: #27b673;
    --brand-green-soft: #5fd39b;
    --brand-blue: #1f7fd1;
    --ink-white: #ffffff;
    --shadow: rgba(20, 30, 40, 0.18);
  }
  * { margin: 0; padding: 0; box-sizing: border-box; }
  html, body { width: 1200px; height: 675px; overflow: hidden; background: var(--stage); }
  .stage {
    position: relative; width: 1200px; height: 675px;
    display: flex; align-items: center; justify-content: center; gap: 40px;
  }
  .card {
    position: relative; width: 520px; height: 298px;
    background: var(--card); border-radius: 26px;
    box-shadow: 0 10px 30px var(--shadow);
    overflow: hidden;
  }
  /* Front side */
  .card-front .brand {
    position: absolute; left: 0; right: 0; top: 104px;
    display: flex; align-items: center; justify-content: center; gap: 14px;
  }
  .brand-square {
    width: 58px; height: 58px; border-radius: 10px; background: var(--brand-green);
  }
  .brand-block { display: flex; flex-direction: column; }
  .brand-name {
    font-family: "Baloo 2", sans-serif; font-weight: 700;
    font-size: 60px; line-height: 0.9; color: var(--brand-green); letter-spacing: 0.5px;
  }
  .brand-tagline {
    font-family: "Ubuntu", sans-serif; font-size: 11px; color: var(--brand-green);
    align-self: flex-end; margin-top: 2px;
  }
  .card-front .website {
    position: absolute; right: 92px; top: 196px;
    font-family: "Ubuntu", sans-serif; font-weight: 500; font-size: 14px; color: var(--brand-green);
  }
  /* Back side */
  .name-tab {
    position: absolute; left: 0; top: 64px; width: 20px; height: 92px;
    background: var(--brand-green-soft);
  }
  .name-band {
    position: absolute; left: 0; top: 84px; width: 300px; height: 88px;
    background: var(--brand-green); border-radius: 0 14px 14px 0;
    color: var(--ink-white); text-align: right; padding: 10px 24px 0 0;
    font-family: "Ubuntu", sans-serif;
  }
  .person-name { font-family: "Baloo 2", sans-serif; font-weight: 600; font-size: 22px; line-height: 1; letter-spacing: 0.6px; margin-right: 20px; }
  .qualification { font-size: 9px; font-style: italic; margin-top: 4px; }
  .job-title { font-size: 11px; margin-top: 10px; }
  .card-back .brand {
    position: absolute; right: 40px; top: 96px;
    display: flex; flex-direction: column; align-items: center; gap: 6px;
  }
  .card-back .brand-square { width: 46px; height: 40px; }
  .card-back .brand-name { font-size: 34px; }
  .contact-list {
    position: absolute; left: 40px; top: 200px; list-style: none;
    font-family: "Ubuntu", sans-serif; font-style: italic; font-size: 13px; color: var(--brand-blue);
  }
  .contact-list li { display: flex; align-items: center; gap: 8px; height: 20px; }
  .contact-icon {
    width: 13px; height: 13px; border-radius: 3px; background: var(--brand-blue);
    display: flex; align-items: center; justify-content: center; flex: none;
  }
  .divider { margin: 0 6px; }
</style>
</head>
<body>
<main class="stage">
  <section class="card card-front" aria-label="Business card front">
    <div class="brand">
      <span class="brand-square"></span>
      <div class="brand-block">
        <span class="brand-name">Zentrova</span>
        <span class="brand-tagline">Creative Automation</span>
      </div>
    </div>
    <p class="website">www.zentrova.com.au</p>
  </section>

  <section class="card card-back" aria-label="Business card back">
    <div class="name-tab"></div>
    <div class="name-band">
      <p class="person-name">Derek Malloway</p>
      <p class="qualification">B Eng ICT (CompSys) Dip EngPrac</p>
      <p class="job-title">Control Systems Programmer</p>
    </div>
    <div class="brand">
      <span class="brand-square"></span>
      <span class="brand-name">Zentrova</span>
    </div>
    <ul class="contact-list">
      <li>
        <span class="contact-icon"><svg width="9" height="9" viewBox="0 0 10 10"><path d="M2 1h2l1 2.5-1.2.8a5 5 0 0 0 2 2l.8-1.2L9 6v2a1 1 0 0 1-1 1A7 7 0 0 1 1 2a1 1 0 0 1 1-1z" fill="#fff"/></svg></span>
        <span>0417 582 90<span class="divider">|</span>024 306 17</span>
      </li>
      <li>
        <span class="contact-icon"><svg width="9" height="9" viewBox="0 0 10 10"><rect x="1" y="2.5" width="8" height="5.5" rx="0.6" fill="none" stroke="#fff" stroke-width="1"/><path d="M1.3 3l3.7 2.6L8.7 3" fill="none" stroke="#fff" stroke-width="1"/></svg></span>
        <span>derekmalloway@zentrova.com.au</span>
      </li>
      <li>
        <span class="contact-icon"><svg width="9" height="9" viewBox="0 0 10 10"><path d="M5 9.5S2 6 2 4a3 3 0 0 1 6 0c0 2-3 5.5-3 5.5z" fill="#fff"/><circle cx="5" cy="4" r="1.1" fill="#1f7fd1"/></svg></span>
        <span>18 Millbrook Lane, Castlereagh, NSW, 2749, Australia</span>
      </li>
    </ul>
  </section>
</main>
</body>
</html>
```